A5 Patient Information Booklet (Chiropractic Clinic) 4-8 pages

Here’s a polished, professional rewrite of your full brief and content, with clearer structure, corrected language, and a premium tone:

---

**Project Title:** Premium Patient Information Brochure (Chiropractic & Wellness Clinic)

---

### **Overview**

We are a health and wellness clinic seeking a premium, high-end patient information brochure to provide following a patient’s initial consultation and first treatment.

The purpose of this booklet is to:

* Reinforce trust and professionalism
* Help patients understand what to expect next
* Encourage adherence to care recommendations
* Position the clinic as calm, expert-led, and results-driven

---

### **Format**

* 4–8 page booklet (A5 or similar size)
* Print-ready and digital versions required

---

### **Target Audience**

Patients who have just completed their initial consultation and may have begun treatment. They may already be experiencing physical or mental changes, so the brochure should guide, reassure, and educate them on what comes next.

---

### **Tone & Style**

* Premium, calm, and reassuring
* Modern wellness aesthetic (not overly clinical)
* Clean layout with minimal clutter
* Soft, neutral colour palette (whites, creams, muted greens, soft blues)
* Elegant typography (e.g. Montserrat / Lato)
* High-end, trustworthy, and professional feel

---

### **Key Messages**

#### 1. Listen to Your Body

Patients may feel different after treatment. Reassure them that this is normal and part of the healing process.

#### 2. Post-Treatment Advice

* Stay well hydrated
* Rest if needed
* Avoid overexertion if the body requires recovery

#### 3. Healing is a Journey (Core Concept)

A strong visual metaphor of a **“road to recovery”** or **journey** should be central to the design.

This journey should clearly illustrate three phases:

* **Phase 1: Initial Care (Weeks 1–6)**
Focus: Reducing pain/discomfort, calming the body, and initiating response to treatment

* **Phase 2: Corrective Care (Weeks 6–12)**
Focus: Addressing underlying issues, improving function, and creating lasting change

* **Phase 3: Wellness / Maintenance (Ongoing)**
Focus: Maintaining progress, preventing relapse, and supporting long-term wellbeing

**Important:**

* Emphasise that this is not a quick fix
* Progress requires time and consistency
* Each patient follows an individualised care plan
* The journey should feel structured, positive, and achievable

#### 4. Personalised Care

Reinforce that every treatment plan is tailored specifically to the individual.

#### 5. Professional Reassurance

Patients should feel confident they are in expert hands and supported throughout their journey.

---

### **Design Direction**

* Use imagery that reflects calmness, progression, and wellness (e.g. pathways, nature, soft gradients)
* Avoid generic stock imagery
* **Only use original clinic images from website and social media**
* Prioritise white space and clarity
* Aim for a luxury spa/medical hybrid aesthetic

---

## **Content Structure (Page-by-Page)**

### **Front Cover**

* Clean, minimal, premium design
* Clinic branding

---

### **Page 1: Patient Case Summary**

**Title:** *Welcome to Fernwell Practice*

Thank you for choosing Fernwell Practice.

This booklet is designed to guide you through:

* What we found during your initial consultation
* Your personalised recommended treatment plan
* Your road to recovery
* Long-term wellness care
* Why we take the approach we do

---

### **Page 2: Your Care Journey**

**Stage 1: Your Initial Consultation**

Today we completed a comprehensive assessment of your health and function, including:

* Full case history and discussion of your symptoms and goals
* Orthopaedic and neurological testing
* Postural and movement assessment
* Initial treatment (where appropriate)

**What this tells us:**

* How your body is currently functioning
* Where areas of stress or dysfunction may be present
* The most appropriate and effective path forward for your care

---

### **Page 3: Your Suggested Treatment Plan**

Based on today’s findings, your recommended care plan is:

**______ treatments over ______ weeks**

This should be viewed alongside your *Road to Recovery* to help you understand what to expect.

We have also discussed:

* Expected timelines for improvement
* Available payment options

**After Treatment:**
It is common to feel different following treatment. This is a normal response as your body begins to adapt and respond.

We recommend:

* Staying well hydrated
* Allowing time for rest and recovery
* Avoiding overexertion if your body feels it needs it

---

### **Page 4: What to Expect Next**

Healing is not always linear—it is a process that occurs over time.

Your care will typically progress through the following stages:

* **Relief Care**
Focused on reducing discomfort and calming the body

* **Corrective Care**
Focused on addressing underlying issues and improving function
(This phase may include prescribed exercises)

* **Maintenance / Wellness Care**
Focused on sustaining progress, preventing recurrence, and supporting long-term health

---

### **Page 5: Understanding Chiropractic Care**

**What is Chiropractic?**
Chiropractic care focuses on the relationship between the spine, nervous system, and overall body function.

By improving spinal movement and alignment, chiropractic care helps support the nervous system, allowing the body to function and heal more effectively.

**About Fernwell Practice**
At Fernwell Practice, our approach is centred around personalised, patient-focused care. We aim to not only relieve symptoms but to address underlying causes and support long-term wellbeing.

---

### **Back Page**

* Clinic contact details
* Website
* Social media icons/handles

**Closing Message:**
“A healthier, stronger you—supported every step of the way.”

---

### **Deliverables**

* Print-ready PDF
* Editable source files

---

### **Additional Notes**

* The brochure should feel valuable and worth keeping
* Encourage long-term care in a subtle, non-pushy way
* Maintain clarity, readability, and strong visual hierarchy
* Balance professionalism with warmth and approachability

---

If you’d like, I can also turn this into **actual brochure copy (fully written, patient-facing text)** or help you refine it further for a designer.

Target Market(s)

Existing patients who want to feel better and look after themselves that is given after their initil consultation appointment

Industry/Entity Type

Chiropractic, wellness, health

Font styles to use
Other font styles liked:
• Montserrat or Lato

Colors
0094D4
00A9DD
6FCCEA
C7EBF8
E9F6FB
00AB8E
00BBA5
67D7C9
C6EFE9
E9F9F6
6B429C
8869AF
B7A5CE
E3DAEB
F3F0F8

Requirements
Must have
• my own photos, look premium wellness, be clear and simple to understand for patients journey or what to expect next and over time
Nice to have
• USe my social media/website for ideas
Should not have
• generic photos and images

```html
<!DOCTYPE html>
<html lang="en">
<head>
<meta charset="utf-8">
<title>Fernwell Practice – Patient Booklet</title>
<link href="https://fonts.googleapis.com/css2?family=Montserrat:wght@300;400;500;600;700&family=Libre+Baskerville:wght@700&display=swap" rel="stylesheet">
<style>
:root{
  --teal:#1fb0aa;
  --teal-dark:#17968f;
  --teal-light:#c6efe9;
  --pink:#e872ae;
  --pink-soft:#f6dbe7;
  --purple:#b7a5ce;
  --blue-soft:#dcedf5;
  --ink:#2a2a2a;
  --grey:#7a7a7a;
  --orange:#e9772f;
  --paper:#ffffff;
  --canvas:#ffffff;
}
*{margin:0;padding:0;box-sizing:border-box}
html,body{width:1200px;height:2593px;overflow:hidden;background:var(--canvas)}
body{position:relative;font-family:'Montserrat',sans-serif;color:var(--ink)}
.page{position:absolute;width:420px;height:610px;background:var(--paper);transform-origin:0 0;overflow:hidden;box-shadow:0 0 14px rgba(0,0,0,.13)}
.page svg.bg{position:absolute;left:0;top:0}
.abs{position:absolute}
.photo{position:absolute;left:0;top:0}
/* brand lockup */
.brand-ring{position:absolute;border-radius:50%;border:5px solid var(--teal);background:#fff}
.brand-name{position:absolute;left:0;width:100%;text-align:center;font-family:'Libre Baskerville',serif;font-weight:700;color:var(--ink);letter-spacing:-.3px;text-transform:uppercase}
/* back cover contact */
.contact{position:absolute;left:0;width:100%;text-align:center;font-size:12.5px;font-weight:600;color:var(--ink)}
.contact-rule{position:absolute;left:98px;width:223px;height:1.5px;background:var(--ink)}
/* chiro page */
.h1{position:absolute;left:43px;font-size:18.5px;font-weight:700;color:#4a4a4a;letter-spacing:.2px}
.h1 em,.h2 em,.journey-title em{font-style:normal;color:var(--teal)}
.lead{position:absolute;left:43px;top:60px;width:348px;font-size:9.15px;line-height:13.1px;font-weight:300;color:#6d6d6d;text-align:justify}
.h2{position:absolute;left:43px;top:400px;font-size:15.5px;font-weight:600;color:#4a4a4a}
.tip{position:absolute;top:433px;height:157px;border-radius:8px}
.tip-listen{left:30px;width:164px;background:linear-gradient(160deg,#d9eef5,#eaf5f3)}
.tip-advice{left:200px;width:203px;background:linear-gradient(160deg,#f8dce8,#f3e6ec)}
.tip h3{position:absolute;left:12px;top:10px;font-size:16.5px;font-weight:500;line-height:21px}
.tip-listen h3{color:var(--teal)}
.tip-advice h3{color:var(--pink)}
.tip h3 span{display:block;padding-left:15px}
.tip p{position:absolute;left:12px;top:66px;width:148px;font-size:9px;line-height:13px;color:#8a8a8a;text-align:justify}
.advice{position:absolute;left:10px;font-size:9.2px;font-weight:600;color:var(--ink);display:flex;gap:8px;align-items:flex-start}
.advice small{display:block;font-size:6.2px;font-weight:400;color:#666;margin-top:2px}
/* journey page */
.panel{position:absolute;left:17px;top:20px;width:380px;height:400px;border-radius:22px;background:linear-gradient(180deg,#d7eaf2,#e6eef4)}
.journey-title{position:absolute;left:0;top:31px;width:414px;text-align:center;font-size:21.5px;font-weight:700;color:#3c3c3c}
.stage-title{position:absolute;font-size:10.5px;font-weight:600;color:#fff;line-height:13px}
.stage-focus{position:absolute;font-size:9px;line-height:11px;color:#eafaf7}
.stage-focus b{font-weight:700;color:#fff}
.important{position:absolute;left:43px;top:430px;font-size:13.5px;font-weight:600;color:var(--ink)}
.bullets{position:absolute;left:43px;top:455px;list-style:none;font-size:8.6px;line-height:15px;color:#555}
.bullets li::before{content:"• "}
.bullets b{font-weight:700;color:var(--ink)}
.pillar{position:absolute;top:528px;font-size:11.5px;font-weight:600}
.pillar-personal{left:43px;color:var(--teal)}
.pillar-reassure{left:200px;color:var(--pink)}
.pillar-text{position:absolute;top:556px;font-size:8.6px;line-height:11px;text-align:justify}
/* personalisation */
.p-box{position:absolute;left:26px;top:143px;width:367px;height:155px;border:2.5px solid var(--pink);border-radius:14px}
.p-title{position:absolute;left:0;top:13px;width:100%;text-align:center;font-size:22px;font-weight:700;color:var(--ink)}
.p-field{position:absolute;left:16px;font-size:9.5px;font-weight:600;color:var(--ink)}
.p-line{position:absolute;height:1px;background:#555}
</style>
</head>
<body>

<!-- ===== Front cover (top) ===== -->
<div class="page cover-front" style="left:178px;top:127px;transform:scale(.986,.99)">
  <svg class="bg" width="420" height="610" viewBox="0 0 420 610">
    <defs>
      <linearGradient id="fc1" x1="1" y1="0" x2="0" y2="1">
        <stop offset="0" stop-color="#8fb3c9"/><stop offset=".45" stop-color="#7a7fa8"/><stop offset="1" stop-color="#c56fa9"/>
      </linearGradient>
    </defs>
    <rect width="420" height="420" fill="url(#fc1)" role="img" aria-label="Photo of the chiropractor treating a patient's back"/>
    <path d="M0 396H118C150 396 142 312 210 306C278 312 270 396 302 396H420V610H0Z" fill="#fff"/>
  </svg>
  <div class="brand-ring" style="left:130px;top:319px;width:156px;height:156px"></div>
  <div class="brand-name" style="top:490px;font-size:32px">Fernwell Practice</div>
</div>

<!-- ===== Back cover (top) ===== -->
<div class="page cover-back" style="left:604px;top:125px;transform:scale(.993,.995)">
  <svg class="bg" width="420" height="610" viewBox="0 0 420 610">
    <defs>
      <linearGradient id="bc1" x1="0" y1="0" x2="0" y2="1">
        <stop offset="0" stop-color="#b9a8d6"/><stop offset="1" stop-color="#ee7cb9"/>
      </linearGradient>
    </defs>
    <rect width="420" height="250" fill="url(#bc1)"/>
    <path d="M0 242H110C142 242 136 158 210 150C284 158 278 242 310 242H420V610H0Z" fill="#fff"/>
  </svg>
  <div class="brand-ring" style="left:130px;top:172px;width:156px;height:156px"></div>
  <div class="brand-name" style="top:340px;font-size:32px">Fernwell Practice</div>
  <div class="contact" style="top:474px">fernwell_practice</div>
  <div class="contact-rule" style="top:504px"></div>
  <div class="contact" style="top:516px;font-size:11.5px">www.fernwellpractice.com</div>
  <div class="contact" style="top:534px;font-size:11.5px">12 Orchard Row, Linford LF4 7QT</div>
</div>

<!-- ===== Chiropractic care page (spread) ===== -->
<div class="page page-chiro" style="left:170px;top:770px;transform:scale(1.012,1.016)">
  <h1 class="h1" style="top:27px">WHAT IS <em>CHIROPRACTIC CARE?</em></h1>
  <p class="lead">Chiropractic care focuses on how your body moves, functions, and heals as a whole. By improving the alignment and mobility of the spine and joints, we help reduce pressure on the nervous system, allowing your body to function more efficiently. Rather than simply masking symptoms, our approach supports your body's natural ability to adapt, recover, and maintain long-term health. Your Chiropractor At Fernwell Practice, your care is led by chiropractor Clara, who takes a personalised, hands-on approach to your health. Every consultation is focused on understanding your body, your lifestyle, and your goals—so your treatment plan is tailored specifically to you. Clara combines clinical expertise with a calm, supportive environment to help you feel confident, informed, and in control of your recovery journey. About Fernwell Practice At Fernwell Practice, we believe that true health is built over time—not achieved through quick fixes. Our approach is centred around personalised care, attention to detail, and long-term results. We work with you to not only relieve symptoms, but to improve how your body functions and performs in everyday life. Every step of your journey is guided with care, clarity, and a focus on lasting wellbeing. What to Expect After Your Treatment It's completely normal to feel different after your treatment. As your body begins to respond and adapt, you may notice changes in movement, tension, or overall wellbeing. Stay Hydrated Drinking plenty of water supports your body's natural recovery process. Listen to Your Body You may feel relief, mild soreness, or changes in how your body moves—these are all normal signs of adjustment. Rest When Needed Give your body time to recover. Avoid overexertion if your body feels it needs rest. Trust the Process Meaningful, lasting change takes time. Each step of your care plan is designed to support long-term results—not just short-term relief.</p>
  <h2 class="h2">WHAT TO EXPECT AFTER <em>YOUR TREATMENT</em></h2>
  <div class="tip tip-listen">
    <h3>1. Listen to<span>Your Body</span></h3>
    <p>Patients may feel different after treatment. Encourage awareness and reassurance that this is normal.</p>
  </div>
  <div class="tip tip-advice">
    <h3>2. Post-Treatment<span>Advice</span></h3>
    <div class="advice" style="top:58px"><svg width="16" height="18" viewBox="0 0 16 18"><path d="M3 2h10l-1.5 14h-7z" fill="none" stroke="var(--teal)" stroke-width="1.4"/><path d="M4.2 8h7.6" stroke="var(--teal)" stroke-width="1.2"/></svg><span style="margin-top:3px">Stay well hydrated</span></div>
    <div class="advice" style="top:91px"><svg width="16" height="16" viewBox="0 0 16 16"><rect x="1.5" y="3" width="13" height="11" rx="2" fill="none" stroke="var(--pink)" stroke-width="1.4"/><path d="M1.5 9h13" stroke="var(--pink)" stroke-width="1.2"/></svg><span style="margin-top:3px">Rest if needed</span></div>
    <div class="advice" style="top:121px"><svg width="16" height="18" viewBox="0 0 16 18"><circle cx="8" cy="4.5" r="3" fill="none" stroke="var(--teal)" stroke-width="1.4"/><path d="M2 17c0-5 2.5-7.5 6-7.5s6 2.5 6 7.5" fill="none" stroke="var(--teal)" stroke-width="1.4"/></svg><span>Avoid overexertion<small>if the body feels like it needs recovery</small></span></div>
  </div>
</div>

<!-- ===== Recovery journey page (spread) ===== -->
<div class="page page-journey" style="left:597px;top:770px;transform:scale(1.007,1.016)">
  <div class="panel"></div>
  <svg class="bg" width="420" height="610" viewBox="0 0 420 610">
    <path d="M170 72C170 110 240 110 238 150C236 190 160 200 170 240C178 275 240 270 236 310C232 350 160 360 172 412" fill="none" stroke="#222" stroke-width="2" stroke-dasharray="6 4"/>
    <g fill="none" stroke="var(--orange)" stroke-width="2"><path d="M152 78l7 6 7-6"/><path d="M152 86l7 6 7-6"/><path d="M152 94l7 6 7-6"/></g>
    <!-- stage 1 -->
    <path d="M34 142H205a18 18 0 0 1 0 36H196V245a10 10 0 0 1-10 10H34a10 10 0 0 1-10-10V152a10 10 0 0 1 10-10z" fill="var(--teal)"/>
    <circle cx="205" cy="160" r="15" fill="#161616" stroke="#fff" stroke-width="3"/>
    <text x="205" y="166" fill="#fff" font-family="Montserrat" font-weight="700" font-size="16" text-anchor="middle">1</text>
    <!-- stage 2 -->
    <path d="M208 220H382a10 10 0 0 1 10 10V324a10 10 0 0 1-10 10H270a10 10 0 0 1-10-10V254H208a17 17 0 0 1 0-34z" fill="var(--pink)"/>
    <circle cx="208" cy="237" r="15" fill="#161616" stroke="#fff" stroke-width="3"/>
    <text x="208" y="243" fill="#fff" font-family="Montserrat" font-weight="700" font-size="16" text-anchor="middle">2</text>
    <!-- stage 3 -->
    <path d="M34 298H206a17 17 0 0 1 0 34H196V400a10 10 0 0 1-10 10H34a10 10 0 0 1-10-10V308a10 10 0 0 1 10-10z" fill="var(--teal)"/>
    <circle cx="206" cy="314" r="15" fill="#161616" stroke="#fff" stroke-width="3"/>
    <text x="206" y="320" fill="#fff" font-family="Montserrat" font-weight="700" font-size="16" text-anchor="middle">3</text>
  </svg>
  <h1 class="journey-title">YOUR RECOVERY <em>JOURNEY</em></h1>
  <div class="stage-title" style="left:37px;top:155px">Initial Care (Weeks 1–6)</div>
  <div class="stage-focus" style="left:37px;top:183px;width:120px"><b>Focus:</b> Reducing pain/discomfort, calming the body, and helping you begin to respond to treatment.</div>
  <div class="stage-title" style="left:245px;top:227px;width:140px">Corrective Care (Weeks 6–12)</div>
  <div class="stage-focus" style="left:262px;top:268px;width:120px;text-align:center"><b>Focus:</b> Addressing underlying issues, improving function, and creating more stable, lasting changes.</div>
  <div class="stage-title" style="left:37px;top:307px">Wellness / Maintenance<br>(Ongoing)</div>
  <div class="stage-focus" style="left:37px;top:347px;width:118px"><b>Focus:</b> Maintaining progress, preventing relapse, and supporting long-term health and wellbeing.</div>
  <div class="important">Important:</div>
  <ul class="bullets">
    <li>This visual should clearly communicate that this is not <b>a quick fix</b></li>
    <li>Progress takes time and consistency</li>
    <li>Each patient will follow an <b>individualised treatment plan</b></li>
    <li>The journey should feel positive, structured, and achievable</li>
  </ul>
  <div class="pillar pillar-personal">4. Personalised Care</div>
  <div class="pillar pillar-reassure">5. Professional Reassurance</div>
  <p class="pillar-text" style="left:43px;width:145px;color:#888">Reinforce that each patient's treatment plan is tailored specifically to them.</p>
  <p class="pillar-text" style="left:200px;width:170px;color:var(--ink)">Patients should feel confident they are in expert hands and supported throughout their journey.</p>
</div>

<!-- ===== Flat page row ===== -->
<div class="page cover-front" style="left:98px;top:1483px;transform:scale(.731,.715)">
  <svg class="bg" width="420" height="610" viewBox="0 0 420 610">
    <defs>
      <linearGradient id="fc2" x1="1" y1="0" x2="0" y2="1">
        <stop offset="0" stop-color="#8fb3c9"/><stop offset=".45" stop-color="#7a7fa8"/><stop offset="1" stop-color="#c56fa9"/>
      </linearGradient>
    </defs>
    <rect width="420" height="420" fill="url(#fc2)" role="img" aria-label="Photo of the chiropractor treating a patient's back"/>
    <path d="M0 396H118C150 396 142 312 210 306C278 312 270 396 302 396H420V610H0Z" fill="#fff"/>
  </svg>
  <div class="brand-ring" style="left:130px;top:319px;width:156px;height:156px"></div>
  <div class="brand-name" style="top:490px;font-size:32px">Fernwell Practice</div>
</div>

<div class="page page-chiro" style="left:439px;top:1483px;transform:scale(.731,.715)">
  <h1 class="h1" style="top:27px">WHAT IS <em>CHIROPRACTIC CARE?</em></h1>
  <p class="lead">Chiropractic care focuses on how your body moves, functions, and heals as a whole. By improving the alignment and mobility of the spine and joints, we help reduce pressure on the nervous system, allowing your body to function more efficiently. Rather than simply masking symptoms, our approach supports your body's natural ability to adapt, recover, and maintain long-term health. Your Chiropractor At Fernwell Practice, your care is led by chiropractor Clara, who takes a personalised, hands-on approach to your health. Every consultation is focused on understanding your body, your lifestyle, and your goals—so your treatment plan is tailored specifically to you. Clara combines clinical expertise with a calm, supportive environment to help you feel confident, informed, and in control of your recovery journey. About Fernwell Practice At Fernwell Practice, we believe that true health is built over time—not achieved through quick fixes. Our approach is centred around personalised care, attention to detail, and long-term results. We work with you to not only relieve symptoms, but to improve how your body functions and performs in everyday life. Every step of your journey is guided with care, clarity, and a focus on lasting wellbeing. What to Expect After Your Treatment It's completely normal to feel different after your treatment. As your body begins to respond and adapt, you may notice changes in movement, tension, or overall wellbeing. Stay Hydrated Drinking plenty of water supports your body's natural recovery process. Listen to Your Body You may feel relief, mild soreness, or changes in how your body moves—these are all normal signs of adjustment. Rest When Needed Give your body time to recover. Avoid overexertion if your body feels it needs rest. Trust the Process Meaningful, lasting change takes time. Each step of your care plan is designed to support long-term results—not just short-term relief.</p>
  <h2 class="h2">WHAT TO EXPECT AFTER <em>YOUR TREATMENT</em></h2>
  <div class="tip tip-listen">
    <h3>1. Listen to<span>Your Body</span></h3>
    <p>Patients may feel different after treatment. Encourage awareness and reassurance that this is normal.</p>
  </div>
  <div class="tip tip-advice">
    <h3>2. Post-Treatment<span>Advice</span></h3>
    <div class="advice" style="top:58px"><svg width="16" height="18" viewBox="0 0 16 18"><path d="M3 2h10l-1.5 14h-7z" fill="none" stroke="var(--teal)" stroke-width="1.4"/><path d="M4.2 8h7.6" stroke="var(--teal)" stroke-width="1.2"/></svg><span style="margin-top:3px">Stay well hydrated</span></div>
    <div class="advice" style="top:91px"><svg width="16" height="16" viewBox="0 0 16 16"><rect x="1.5" y="3" width="13" height="11" rx="2" fill="none" stroke="var(--pink)" stroke-width="1.4"/><path d="M1.5 9h13" stroke="var(--pink)" stroke-width="1.2"/></svg><span style="margin-top:3px">Rest if needed</span></div>
    <div class="advice" style="top:121px"><svg width="16" height="18" viewBox="0 0 16 18"><circle cx="8" cy="4.5" r="3" fill="none" stroke="var(--teal)" stroke-width="1.4"/><path d="M2 17c0-5 2.5-7.5 6-7.5s6 2.5 6 7.5" fill="none" stroke="var(--teal)" stroke-width="1.4"/></svg><span>Avoid overexertion<small>if the body feels like it needs recovery</small></span></div>
  </div>
</div>

<div class="page page-journey" style="left:780px;top:1483px;transform:scale(.731,.715)">
  <div class="panel"></div>
  <svg class="bg" width="420" height="610" viewBox="0 0 420 610">
    <path d="M170 72C170 110 240 110 238 150C236 190 160 200 170 240C178 275 240 270 236 310C232 350 160 360 172 412" fill="none" stroke="#222" stroke-width="2" stroke-dasharray="6 4"/>
    <g fill="none" stroke="var(--orange)" stroke-width="2"><path d="M152 78l7 6 7-6"/><path d="M152 86l7 6 7-6"/><path d="M152 94l7 6 7-6"/></g>
    <path d="M34 142H205a18 18 0 0 1 0 36H196V245a10 10 0 0 1-10 10H34a10 10 0 0 1-10-10V152a10 10 0 0 1 10-10z" fill="var(--teal)"/>
    <circle cx="205" cy="160" r="15" fill="#161616" stroke="#fff" stroke-width="3"/>
    <text x="205" y="166" fill="#fff" font-family="Montserrat" font-weight="700" font-size="16" text-anchor="middle">1</text>
    <path d="M208 220H382a10 10 0 0 1 10 10V324a10 10 0 0 1-10 10H270a10 10 0 0 1-10-10V254H208a17 17 0 0 1 0-34z" fill="var(--pink)"/>
    <circle cx="208" cy="237" r="15" fill="#161616" stroke="#fff" stroke-width="3"/>
    <text x="208" y="243" fill="#fff" font-family="Montserrat" font-weight="700" font-size="16" text-anchor="middle">2</text>
    <path d="M34 298H206a17 17 0 0 1 0 34H196V400a10 10 0 0 1-10 10H34a10 10 0 0 1-10-10V308a10 10 0 0 1 10-10z" fill="var(--teal)"/>
    <circle cx="206" cy="314" r="15" fill="#161616" stroke="#fff" stroke-width="3"/>
    <text x="206" y="320" fill="#fff" font-family="Montserrat" font-weight="700" font-size="16" text-anchor="middle">3</text>
  </svg>
  <h1 class="journey-title">YOUR RECOVERY <em>JOURNEY</em></h1>
  <div class="stage-title" style="left:37px;top:155px">Initial Care (Weeks 1–6)</div>
  <div class="stage-focus" style="left:37px;top:183px;width:120px"><b>Focus:</b> Reducing pain/discomfort, calming the body, and helping you begin to respond to treatment.</div>
  <div class="stage-title" style="left:245px;top:227px;width:140px">Corrective Care (Weeks 6–12)</div>
  <div class="stage-focus" style="left:262px;top:268px;width:120px;text-align:center"><b>Focus:</b> Addressing underlying issues, improving function, and creating more stable, lasting changes.</div>
  <div class="stage-title" style="left:37px;top:307px">Wellness / Maintenance<br>(Ongoing)</div>
  <div class="stage-focus" style="left:37px;top:347px;width:118px"><b>Focus:</b> Maintaining progress, preventing relapse, and supporting long-term health and wellbeing.</div>
  <div class="important">Important:</div>
  <ul class="bullets">
    <li>This visual should clearly communicate that this is not <b>a quick fix</b></li>
    <li>Progress takes time and consistency</li>
    <li>Each patient will follow an <b>individualised treatment plan</b></li>
    <li>The journey should feel positive, structured, and achievable</li>
  </ul>
  <div class="pillar pillar-personal">4. Personalised Care</div>
  <div class="pillar pillar-reassure">5. Professional Reassurance</div>
  <p class="pillar-text" style="left:43px;width:145px;color:#888">Reinforce that each patient's treatment plan is tailored specifically to them.</p>
  <p class="pillar-text" style="left:200px;width:170px;color:var(--ink)">Patients should feel confident they are in expert hands and supported throughout their journey.</p>
</div>

<!-- ===== Personalisation page ===== -->
<div class="page page-personal" style="left:272px;top:1962px;transform:scale(.731,.715)">
  <div class="brand-ring" style="left:181px;top:30px;width:58px;height:58px;border-width:3px"></div>
  <div class="brand-name" style="top:96px;font-size:15px">Fernwell Practice</div>
  <div class="p-box">
    <div class="p-title">PERSONALISATION SECTION</div>
    <div class="p-field" style="top:52px">Patient Name:</div>
    <div class="p-line" style="left:92px;right:16px;top:63px"></div>
    <div class="p-field" style="top:82px">Your Suggested Care Plan:</div>
    <div class="p-line" style="left:16px;right:16px;top:106px"></div>
    <div class="p-field" style="top:125px">treatments over <span style="display:inline-block;width:80px;border-bottom:1px solid #555"></span> weeks.</div>
  </div>
  <div class="abs" role="img" aria-label="Photo of a spine anatomy print on a desk" style="left:27px;top:316px;width:364px;height:264px;border-radius:20px;background:linear-gradient(135deg,#d9d4cc 0%,#eeece8 45%,#f4f3f0 70%,#e2dfda 100%)"></div>
</div>

<!-- ===== Back cover (flat) ===== -->
<div class="page cover-back" style="left:619px;top:1962px;transform:scale(.731,.715)">
  <svg class="bg" width="420" height="610" viewBox="0 0 420 610">
    <defs>
      <linearGradient id="bc2" x1="0" y1="0" x2="0" y2="1">
        <stop offset="0" stop-color="#b9a8d6"/><stop offset="1" stop-color="#ee7cb9"/>
      </linearGradient>
    </defs>
    <rect width="420" height="250" fill="url(#bc2)"/>
    <path d="M0 242H110C142 242 136 158 210 150C284 158 278 242 310 242H420V610H0Z" fill="#fff"/>
  </svg>
  <div class="brand-ring" style="left:130px;top:172px;width:156px;height:156px"></div>
  <div class="brand-name" style="top:340px;font-size:32px">Fernwell Practice</div>
  <div class="contact" style="top:474px">fernwell_practice</div>
  <div class="contact-rule" style="top:504px"></div>
  <div class="contact" style="top:516px;font-size:11.5px">www.fernwellpractice.com</div>
  <div class="contact" style="top:534px;font-size:11.5px">12 Orchard Row, Linford LF4 7QT</div>
</div>

</body>
</html>
```